Business Card Design of an established Waste Management, Plastic Recycling and Renewable Energy Comp

We are looking for business card design for plastic card with holograms (Very similar to credit card). I will provide our logo (Quillbys). So the name on the business card will be our logo )Quillbys) + Environmental next to it, so it will read Quillbys Environmental. The font for Environmental does not to be the same as the font of the logo. The holograms will be used to display ISO14001 Certified (In normal credit card, normally on the holograms, they show orbis or plex). I will post the design requirements from the card printing company very shortly to make sure they can use the design for the plastic card.

Target Market(s)

Companies, Government Organizations, Corporations.

Industry/Entity Type

Business

Contact Information for Business Card

Motto (Under the logo): Waste Made Right
Name: Bertolomeus Kesslani; Position: Business Manager; Address: Fernwick Landfill & Recycling Facility, Tallowmere Rd, Emberfield, WA 6231; Ph: +61 8 6100 4213; Mob: +61 400 917 358; E: Bertram@quillbysenvironmental.com

Requirements
Must have
• Business Names: Quillbys Logo + Environmental word after the logo.
• Motto (Under the logo): Waste Made Right
• All the Business Card Details above.
• Hologram Logo on the lower right corner which says: ISO 14001 Certified.
• Please remember the design will be printed on plastic card Not paper. The plastic crad is the same as credit card. Hope this helps. Thank You

```html
<!DOCTYPE html>
<html lang="en">
<head>
<meta charset="utf-8">
<title>Quillbys Environmental – Business Card</title>
<link href="https://fonts.googleapis.com/css2?family=Open+Sans:wght@400;600;700&display=swap" rel="stylesheet">
<style>
  :root {
    --backdrop: #2a2b2d;
    --card: #c8cbcd;
    --card-edge: #dfe2e4;
    --ink: #4e5257;
    --ink-soft: #6b7075;
    --accent: #2aa3e0;
    --hologram: #9aa0a4;
  }
  * { margin: 0; padding: 0; box-sizing: border-box; }
  html, body {
    width: 1200px; height: 800px; overflow: hidden;
    background: var(--backdrop);
    font-family: "Open Sans", Arial, sans-serif;
  }
  .stage {
    width: 1200px; height: 800px;
    display: flex; align-items: center; justify-content: center; gap: 40px;
  }
  .card {
    position: relative;
    width: 540px; height: 340px;
    border-radius: 20px;
    background: linear-gradient(160deg, var(--card-edge) 0%, var(--card) 55%, #bdc1c4 100%);
    box-shadow: 0 14px 30px rgba(0,0,0,.45);
    color: var(--ink);
    overflow: hidden;
  }

  /* Front */
  .brand { position: absolute; left: 34px; top: 30px; }
  .brand-row { display: flex; align-items: center; gap: 10px; }
  .brand-mark { width: 30px; height: 30px; border-radius: 50%; background: var(--accent); flex: none; }
  .brand-name { font-size: 34px; font-weight: 700; line-height: 1; color: var(--ink); letter-spacing: .5px; }
  .brand-sub { font-size: 19px; font-weight: 700; color: var(--ink); margin: 4px 0 0 40px; line-height: 1; }
  .motto { font-size: 14px; color: var(--ink-soft); margin: 4px 0 0 40px; }

  .contacts { position: absolute; left: 34px; top: 150px; list-style: none; }
  .contacts li { display: flex; align-items: center; gap: 10px; font-size: 12.5px; line-height: 19px; color: var(--ink); white-space: nowrap; }
  .contacts svg { width: 14px; height: 14px; flex: none; fill: var(--accent); }
  .contacts .indent { padding-left: 24px; }

  .website { position: absolute; left: 130px; top: 278px; display: flex; align-items: center; gap: 10px; font-size: 13px; color: var(--ink); }
  .website svg { width: 16px; height: 16px; }

  .hologram {
    position: absolute; right: 40px; bottom: 28px;
    width: 52px; height: 52px; border-radius: 4px;
    border: 2px solid var(--hologram);
    background: linear-gradient(135deg, #d5d9dc, #b2b8bc);
  }

  /* Back */
  .back-brand { position: absolute; left: 0; right: 0; top: 112px; display: flex; justify-content: center; align-items: center; gap: 12px; }
  .back-brand .brand-mark { width: 42px; height: 42px; }
  .back-brand .brand-name { font-size: 52px; }
  .holder { position: absolute; right: 44px; bottom: 56px; text-align: right; }
  .holder-name { font-size: 18px; font-weight: 600; color: var(--ink); }
  .holder-role { font-size: 12.5px; color: var(--ink-soft); margin-top: 2px; }
</style>
</head>
<body>
<main class="stage">

  <section class="card card-front" aria-label="Card front">
    <header class="brand">
      <div class="brand-row">
        <span class="brand-mark"></span>
        <span class="brand-name">Quillbys</span>
      </div>
      <div class="brand-sub">Environmental</div>
      <p class="motto">Waste Made Right</p>
    </header>

    <ul class="contacts">
      <li>
        <svg viewBox="0 0 24 24"><path d="M12 2a7 7 0 0 0-7 7c0 5 7 13 7 13s7-8 7-13a7 7 0 0 0-7-7zm0 9.5A2.5 2.5 0 1 1 12 6.5a2.5 2.5 0 0 1 0 5z"/></svg>
        Fernwick Landfill &amp; Recycling Facility,
      </li>
      <li class="indent">Tallowmere Rd, Emberfield, WA 6231.</li>
      <li>
        <svg viewBox="0 0 24 24"><path d="M6.6 10.8a15 15 0 0 0 6.6 6.6l2.2-2.2a1 1 0 0 1 1-.25 11.4 11.4 0 0 0 3.6.57 1 1 0 0 1 1 1V20a1 1 0 0 1-1 1A17 17 0 0 1 3 4a1 1 0 0 1 1-1h3.5a1 1 0 0 1 1 1c0 1.25.2 2.45.57 3.6a1 1 0 0 1-.25 1z"/></svg>
        +61 8 6100 4213
      </li>
      <li>
        <svg viewBox="0 0 24 24"><path d="M7 1h10a2 2 0 0 1 2 2v18a2 2 0 0 1-2 2H7a2 2 0 0 1-2-2V3a2 2 0 0 1 2-2zm0 3v14h10V4zm5 15.5a1 1 0 1 0 0 2 1 1 0 0 0 0-2z"/></svg>
        +61 400 917 358
      </li>
      <li>
        <svg viewBox="0 0 24 24"><path d="M2 5h20v14H2zm2 2v.5l8 5 8-5V7zm0 2.8V17h16V9.8l-8 5z"/></svg>
        Bertram@quillbysenvironmental.com
      </li>
    </ul>

    <div class="website">
      <svg viewBox="0 0 24 24" fill="none" stroke="var(--accent)" stroke-width="2"><circle cx="12" cy="12" r="9"/><path d="M3 12h18M12 3c3 3 3 15 0 18M12 3c-3 3-3 15 0 18"/></svg>
      www.quillbysgroup.com
    </div>

    <div class="hologram" aria-label="Certification hologram"></div>
  </section>

  <section class="card card-back" aria-label="Card back">
    <div class="back-brand">
      <span class="brand-mark"></span>
      <span class="brand-name">Quillbys</span>
    </div>
    <div class="holder">
      <p class="holder-name">Bertolomeus Kesslani</p>
      <p class="holder-role">Business Manager</p>
    </div>
  </section>

</main>
</body>
</html>
```